STOREFRONT SIGNAGE/ NEW LOGO

Looking for someone to enhance my current sign idea. I own a pawn shop , which is also a gun shop. I want a catchy front sign, which will be a lighted box sign. I may want to incorporate some symbols or character symbology that highlight firearms, such as : guns, ammo, targets, scope retical , gold, diamonds, cash, watches and/or pawn balls, and im open to other ideas, but i do not want it too busy, i want it simple, with a twist. Attached, you will find a very basic design, showing the business name and the verbiage that I would like to be incorporated into the design. God bless and thank you. may the best design win !

```html
<!DOCTYPE html>
<html lang="en">
<head>
<meta charset="utf-8">
<title>Keystone Exchange — Storefront Sign</title>
<link href="https://fonts.googleapis.com/css2?family=Montserrat:wght@700;800&display=swap" rel="stylesheet">
<style>
  :root {
    --backdrop: #403c3e;
    --panel-light: #f4f4f4;
    --panel-shade: #cfcfcf;
    --sign-red: #ff0000;
    --gold: #b8892c;
    --gold-soft: #e0b04e;
    --ink: #1e1e1e;
    --white: #ffffff;
    --outline: #000000;
  }
  * { margin: 0; padding: 0; box-sizing: border-box; }
  html, body { width: 1200px; height: 1200px; overflow: hidden; background: var(--backdrop); }
  .canvas { position: relative; width: 1200px; height: 1200px; font-family: "Montserrat", sans-serif; }
  .sign { position: absolute; left: 35px; top: 514px; width: 1130px; height: 188px; }
  .sign-shapes { position: absolute; inset: 0; }

  .brand {
    position: absolute; left: 0; top: 0; width: 830px; height: 143px;
    display: flex; align-items: center; justify-content: center; gap: 26px;
  }
  .brand__mark { width: 96px; height: 96px; border-radius: 50%; background: var(--gold); flex: none; }
  .brand__name {
    font-weight: 800; font-size: 62px; line-height: 0.98; color: var(--ink);
    letter-spacing: 0; text-transform: uppercase;
  }

  .tagline {
    position: absolute; left: 35px; top: 148px; font-weight: 700; font-size: 38px;
    letter-spacing: 1.5px; line-height: 1; white-space: nowrap;
  }
  .tagline__gold { color: var(--gold-soft); }
  .tagline__guns { color: var(--white); }

  .services { position: absolute; left: 902px; top: 10px; list-style: none; }
  .service { display: flex; align-items: center; height: 34.6px; }
  .service__icon { width: 30px; height: 30px; margin-right: 8px; flex: none; }
  .service__label { font-weight: 700; font-size: 28px; color: var(--white); letter-spacing: 1px; line-height: 1; }
</style>
</head>
<body>
<div class="canvas">
  <div class="sign">
    <svg class="sign-shapes" width="1130" height="188" viewBox="0 0 1130 188">
      <defs>
        <linearGradient id="panelGrad" x1="0" y1="0" x2="0" y2="1">
          <stop offset="0" stop-color="var(--panel-shade)"/>
          <stop offset="0.8" stop-color="var(--panel-light)"/>
        </linearGradient>
      </defs>
      <rect x="0" y="0" width="1130" height="188" fill="var(--sign-red)"/>
      <path d="M0 0 H893 L845 125 Q838 143 818 143 H0 Z" fill="url(#panelGrad)"/>
      <path d="M893 0 H898 L850 126 Q842 147 818 147 H0 V143 H818 Q838 143 845 125 Z" fill="var(--outline)"/>
    </svg>

    <div class="brand">
      <span class="brand__mark"></span>
      <p class="brand__name">Keystone<br>Exchange</p>
    </div>

    <p class="tagline"><span class="tagline__gold">CASH FOR GOLD</span><span class="tagline__guns">......CASH FOR GUNS</span></p>

    <ul class="services">
      <li class="service">
        <svg class="service__icon" viewBox="0 0 30 30"><circle cx="15" cy="15" r="14" fill="var(--white)"/><circle cx="15" cy="15" r="12" fill="none" stroke="var(--sign-red)" stroke-width="1.2"/><path d="M8 10 H22 M15 10 V14" stroke="var(--sign-red)" stroke-width="1.5"/><circle cx="10" cy="17" r="3" fill="var(--sign-red)"/><circle cx="20" cy="17" r="3" fill="var(--sign-red)"/><circle cx="15" cy="21" r="3" fill="var(--sign-red)"/></svg>
        <span class="service__label">PAWN</span>
      </li>
      <li class="service">
        <svg class="service__icon" viewBox="0 0 30 30"><circle cx="15" cy="15" r="14" fill="var(--white)"/><circle cx="15" cy="15" r="12" fill="none" stroke="var(--sign-red)" stroke-width="1.2"/><path d="M7 10 H10 L12 18 H21 L23 12 H11" fill="none" stroke="var(--sign-red)" stroke-width="1.6"/><circle cx="13" cy="21" r="1.5" fill="var(--sign-red)"/><circle cx="20" cy="21" r="1.5" fill="var(--sign-red)"/></svg>
        <span class="service__label">BUY</span>
      </li>
      <li class="service">
        <svg class="service__icon" viewBox="0 0 30 30"><circle cx="15" cy="15" r="14" fill="var(--white)"/><circle cx="15" cy="15" r="12" fill="none" stroke="var(--sign-red)" stroke-width="1.2"/><path d="M7 11 H10 L12 19 H21 L23 13" fill="none" stroke="var(--sign-red)" stroke-width="1.6"/><path d="M16.5 16 V9 M13.5 12 L16.5 8.5 L19.5 12" fill="none" stroke="var(--sign-red)" stroke-width="1.6"/><circle cx="13" cy="22" r="1.5" fill="var(--sign-red)"/><circle cx="20" cy="22" r="1.5" fill="var(--sign-red)"/></svg>
        <span class="service__label">SELL</span>
      </li>
      <li class="service">
        <svg class="service__icon" viewBox="0 0 30 30"><circle cx="15" cy="15" r="14" fill="var(--white)"/><circle cx="15" cy="15" r="12" fill="none" stroke="var(--sign-red)" stroke-width="1.2"/><path d="M7 15 L12 10 L16 13 L19 10 L23 15 L17 21 L12 17 Z" fill="none" stroke="var(--sign-red)" stroke-width="1.6" stroke-linejoin="round"/></svg>
        <span class="service__label">TRADE</span>
      </li>
      <li class="service">
        <svg class="service__icon" viewBox="0 0 30 30"><circle cx="15" cy="15" r="14" fill="var(--white)"/><circle cx="15" cy="15" r="12" fill="none" stroke="var(--sign-red)" stroke-width="1.2"/><rect x="10" y="7" width="10" height="15" fill="none" stroke="var(--sign-red)" stroke-width="1.6"/><path d="M12 12 H18 M12 15 H18 M12 18 H16" stroke="var(--sign-red)" stroke-width="1.3"/></svg>
        <span class="service__label">LAYAWAY</span>
      </li>
    </ul>
  </div>
</div>
</body>
</html>
```